indépendant en tant que Massothérapeute et Préparateur Mental, j'ai besoin de ...

Massothérapeute et préparateur mental indépendant, je recherche une carte de visite sobre et dynamique, sans images liées au massage ou à la préparation mentale mais intégrant mon logo. Les couleurs que j'aime bien sont : Blanc, gris, anthracite, noir et jaune

Contact Information for Business Card

carte de préférence Horizontale
neutre qui puisse toucher le deux domaines Massothérapie et préparation mentale

Requirements
Must have
• mon projet doit intégrer au recto:
LOGO
Loïc Vermande
078 315 26 49
info@loicvermande-exemple.ch
et éventuellement www.loicvermande-exemple.ch

et au verso les deux adresses:

Chemin des Ormelets 27B
1400 Yverdon-les-Bains

Rue des Tanneries 9
1700 Fribourg

Should not have
• mon projet ne doit pas contenir d'image en liens avec le massage ni la préparation mentale.

```html
<!DOCTYPE html>
<html lang="fr">
<head>
<meta charset="utf-8">
<title>Loïc Vermande – Cartes de visite</title>
<link rel="stylesheet" href="https://fonts.googleapis.com/css2?family=Lato:wght@400;700;900&display=swap">
<style>
  :root {
    --backdrop: #d9d6d2;
    --card: #2c2c2e;
    --card-edge: #232325;
    --ink-white: #f4f4f4;
    --ink-grey: #c9c9c9;
    --ink-soft: #38383b;
    --ink-dark: #1a1a1b;
    --accent-yellow: #f2b41a;
  }
  * { box-sizing: border-box; margin: 0; padding: 0; }
  html, body { width: 1200px; height: 795px; overflow: hidden; }
  body {
    background: var(--backdrop);
    font-family: "Lato", Arial, sans-serif;
    position: relative;
  }
  .card {
    position: absolute;
    top: 240px;
    width: 540px;
    height: 310px;
    background: var(--card);
    border-radius: 4px;
    box-shadow: 0 2px 0 var(--card-edge), 0 14px 30px rgba(0,0,0,.25);
    overflow: hidden;
  }
  .card--back { left: 40px; }
  .card--front { left: 620px; }

  .brand { position: absolute; }
  .brand__name {
    font-weight: 900;
    text-transform: uppercase;
    letter-spacing: .06em;
    line-height: 1;
  }
  .brand__tagline {
    font-size: 8px;
    text-transform: uppercase;
    letter-spacing: .08em;
    margin-top: 5px;
  }
  .card--back .brand { left: 110px; top: 62px; }
  .card--back .brand__name { font-size: 30px; color: var(--ink-dark); }
  .card--back .brand__tagline { color: var(--ink-dark); }

  .addresses {
    position: absolute;
    left: 60px;
    top: 170px;
    list-style: none;
  }
  .addresses li {
    display: flex;
    align-items: center;
    gap: 8px;
    color: var(--ink-grey);
    font-size: 15px;
    margin-bottom: 10px;
  }
  .addresses li + li { margin-left: 26px; }

  .card--front .brand { left: 40px; top: 34px; }
  .card--front .brand__name { font-size: 30px; color: var(--ink-white); }
  .card--front .brand__tagline { color: var(--ink-white); }

  .holder { position: absolute; left: 40px; top: 118px; color: var(--ink-white); }
  .holder__name { font-size: 20px; font-weight: 700; text-transform: uppercase; }
  .holder__role { font-size: 16px; margin-top: 2px; }

  .contacts { position: absolute; left: 40px; top: 188px; list-style: none; z-index: 1; }
  .contacts li {
    display: flex;
    align-items: center;
    gap: 8px;
    color: var(--ink-white);
    font-size: 15px;
    margin-bottom: 6px;
  }
  .icon { width: 12px; height: 12px; flex: none; }

  .watermark-name {
    position: absolute;
    right: 26px;
    bottom: 22px;
    width: 220px;
    font-size: 38px;
    font-weight: 900;
    text-transform: uppercase;
    text-align: right;
    color: var(--ink-soft);
    letter-spacing: .02em;
    line-height: 1.05;
  }
  .watermark-name span { display: block; }
</style>
</head>
<body>

<section class="card card--back" aria-label="Verso">
  <div class="brand">
    <p class="brand__name">Loïc Vermande</p>
    <p class="brand__tagline">Massothérapeute / Préparateur Mental</p>
  </div>
  <ul class="addresses">
    <li>
      <svg class="icon" viewBox="0 0 12 12" aria-hidden="true"><path d="M6 0a4 4 0 0 0-4 4c0 3 4 8 4 8s4-5 4-8a4 4 0 0 0-4-4zm0 5.5A1.5 1.5 0 1 1 6 2.5a1.5 1.5 0 0 1 0 3z" fill="var(--accent-yellow)"/></svg>
      Chemin des Ormelets 27B, 1400 Yverdon-les-Bains
    </li>
    <li>
      <svg class="icon" viewBox="0 0 12 12" aria-hidden="true"><path d="M6 0a4 4 0 0 0-4 4c0 3 4 8 4 8s4-5 4-8a4 4 0 0 0-4-4zm0 5.5A1.5 1.5 0 1 1 6 2.5a1.5 1.5 0 0 1 0 3z" fill="var(--accent-yellow)"/></svg>
      Rue des Tanneries 9, 1700 Freiburg
    </li>
  </ul>
</section>

<section class="card card--front" aria-label="Recto">
  <div class="brand">
    <p class="brand__name">Loïc Vermande</p>
    <p class="brand__tagline">Massothérapeute / Préparateur Mental</p>
  </div>
  <div class="holder">
    <p class="holder__name">Loïc Vermande</p>
    <p class="holder__role">Founder &amp; CEO</p>
  </div>
  <ul class="contacts">
    <li>
      <svg class="icon" viewBox="0 0 12 12" aria-hidden="true"><path d="M2.5 1l2 2-1 1.5a7 7 0 0 0 4 4L9 7.5l2 2-1.5 1.5C5 11 1 7 1 2.5z" fill="var(--accent-yellow)"/></svg>
      078 315 26 49
    </li>
    <li>
      <svg class="icon" viewBox="0 0 12 12" aria-hidden="true"><rect x="0.5" y="2" width="11" height="8" fill="var(--accent-yellow)"/><path d="M0.5 2l5.5 4.5L11.5 2" fill="none" stroke="var(--card)" stroke-width="1"/></svg>
      info@loicvermande-exemple.ch
    </li>
    <li>
      <svg class="icon" viewBox="0 0 12 12" aria-hidden="true"><circle cx="6" cy="6" r="5.5" fill="var(--accent-yellow)"/><path d="M0.5 6h11M6 0.5c-3 3-3 8 0 11M6 0.5c3 3 3 8 0 11" fill="none" stroke="var(--card)" stroke-width=".8"/></svg>
      www.loicvermande-exemple.ch
    </li>
  </ul>
  <p class="watermark-name" aria-hidden="true"><span>Loïc</span><span>Vermande</span></p>
</section>

</body>
</html>
```